Redesign of Engineering firm website

I want a redesign of the velkorpower.com website with the below in mind:

1- the client has a 3 main sectors: Renewable Energy, Process Automation and General Engineering.
2- Home page should show the 3 sectors
3- the other standard pages should be home, About, Clients, Projects, Training, Career, and Contact
4- The theme should be wordpress.
5- Responsive layout that works with all devices
6- One page layout is preferable for the home page.
7- it should be original and is not copied from other templates.

Target Market(s)

Engineers and professional

Industry/Entity Type

Solar Energy

Font styles to use
Serif
Sans Serif

Colors
3277b5
0355a3
0493ce

Requirements
Must have
• pictures that represent the three sectors

```html
<!DOCTYPE html>
<html lang="en">
<head>
<meta charset="utf-8">
<title>Velkor Power Consulting</title>
<link href="https://fonts.googleapis.com/css2?family=Open+Sans:wght@400;600;700&display=swap" rel="stylesheet">
<style>
:root{
  --blue:#0493ce;
  --blue-mid:#3277b5;
  --blue-deep:#0355a3;
  --accent:#f2c230;
  --ink:#222;
  --muted:#777;
  --panel:#f4f4f4;
  --footer:#1d2027;
  --bottom:#050505;
  --white:#fff;
}
*{box-sizing:border-box;margin:0;padding:0}
html,body{width:1200px;height:2473px;overflow:hidden}
body{position:relative;font-family:"Open Sans",Arial,sans-serif;color:var(--ink);background:var(--white)}
.abs{position:absolute}
.photo{position:absolute;display:block}

/* hero */
.hero{position:absolute;left:0;top:0;width:1200px;height:659px;
  background:radial-gradient(ellipse at 50% 55%,#4d6b2a 0%,#24381f 35%,#111a22 70%,#0b1119 100%)}
.topline{position:absolute;left:0;top:0;width:1200px;height:5px;background:var(--blue)}
.brand{position:absolute;left:91px;top:40px;font-size:34px;font-weight:700;color:var(--blue);letter-spacing:1px;display:flex;align-items:center;gap:10px}
.brand .dot{width:14px;height:14px;background:var(--accent)}
.nav{position:absolute;top:50px;left:368px;display:flex;gap:0;font-size:15px;color:var(--white)}
.nav a{color:var(--white);text-decoration:none;position:absolute;white-space:nowrap}
.nav a.active{color:var(--accent)}
.login{position:absolute;left:1005px;top:42px;width:107px;height:37px;border:1.5px solid var(--white);border-radius:19px;color:var(--white);font-size:15px;display:flex;align-items:center;justify-content:center}
.hero-title{position:absolute;left:0;width:1200px;top:288px;text-align:center;color:var(--white);font-size:45px;font-weight:600;text-shadow:0 2px 6px rgba(0,0,0,.5)}
.hero-sub{position:absolute;left:0;width:1200px;top:338px;text-align:center;color:var(--white);font-size:27px}
.arrow-btn{position:absolute;top:325px;width:36px;height:36px;border-radius:50%;background:rgba(0,0,0,.55)}

/* sectors */
.sectors{position:absolute;left:87px;top:587px;width:1025px;height:356px;background:var(--white);box-shadow:0 2px 8px rgba(0,0,0,.25)}
.sector{position:absolute;top:21px;width:320px}
.sector .photo{position:relative;width:320px;height:191px;border:3px solid #eee}
.sector h3{font-size:18px;font-weight:400;margin-top:22px;color:#333}
.sector p{font-size:13.5px;color:var(--muted);line-height:23px;margin-top:6px}
.sector .more{font-size:13px;color:var(--blue);margin-top:6px;display:block}

/* welcome */
.welcome{position:absolute;left:0;top:999px;width:1200px;height:395px;background:var(--panel)}
.welcome h2{position:absolute;left:89px;top:101px;font-size:26px;font-weight:400}
.welcome p{position:absolute;left:89px;top:142px;width:517px;font-size:13px;color:var(--muted);line-height:21.5px;text-align:justify}
.readmore{position:absolute;left:89px;top:286px;width:105px;height:33px;border:1.5px solid var(--blue-mid);border-radius:17px;font-size:13px;color:var(--blue-mid);display:flex;align-items:center;justify-content:center}
.welcome .frame{position:absolute;left:654px;top:80px;width:460px;height:262px;border:3px solid #e2e2e2;background:var(--white)}

/* projects */
.section-title{position:absolute;left:0;width:1200px;text-align:center;font-weight:400}
.project{position:absolute;top:1567px;width:242px;height:193px;background:var(--white);box-shadow:0 1px 4px rgba(0,0,0,.25)}
.project .photo{width:242px;height:144px}
.project .cap{height:49px;display:flex;align-items:center;justify-content:center;font-size:13.5px;color:#333}

/* news */
.news{position:absolute;left:0;top:1839px;width:1200px;height:330px;background:var(--panel)}
.item{position:absolute;top:125px}
.item .photo{position:absolute;left:0;top:0;width:161px;height:142px}
.item .body{position:absolute;left:176px;top:14px;width:310px}
.item h4{font-size:15.5px;font-weight:400;color:#333}
.item .date{font-size:12.5px;color:#555;margin-top:5px}
.item p{font-size:12px;color:#555;line-height:19px;margin-top:4px;text-align:justify}
.item .link{font-size:12.5px;color:var(--blue);margin-top:4px;display:block}

/* footer */
.footer{position:absolute;left:0;top:2170px;width:1200px;height:220px;background:var(--footer);color:var(--white)}
.footer h5{font-size:14.5px;font-weight:400;position:absolute;top:50px}
.footer .col{position:absolute;font-size:12px;line-height:22px}
.email{position:absolute;left:656px;top:130px;width:147px;height:30px;background:var(--white);color:#888;font-size:12px;padding:7px 8px}
.submit{position:absolute;left:803px;top:130px;width:56px;height:30px;background:var(--blue);color:var(--white);font-size:12px;display:flex;align-items:center;justify-content:center}
.social{position:absolute;top:2277px;width:26px;height:26px;background:var(--white);border-radius:4px}
.bottom{position:absolute;left:0;top:2390px;width:1200px;height:83px;background:var(--bottom);color:var(--white);font-size:13px;text-align:center;line-height:93px}
</style>
</head>
<body>

<header class="hero" role="img" aria-label="Dark green scene of a power plug, globe, trees, wind turbines and a solar panel">
</header>
<div class="topline"></div>
<div class="brand"><span class="dot"></span>VELKOR</div>
<nav class="nav">
  <a class="active" style="left:0">HOME</a>
  <a style="left:79px">ABOUT</a>
  <a style="left:164px">CLIENTS</a>
  <a style="left:255px">PROJECTS</a>
  <a style="left:358px">TRAINING</a>
  <a style="left:460px">CAREER</a>
  <a style="left:549px">CONTACT</a>
</nav>
<div class="login">LOG IN</div>
<h1 class="hero-title">VELKOR POWER CONSULTING</h1>
<div class="hero-sub">Neque porro quisquam est qui dolorem</div>
<div class="arrow-btn" style="left:63px"><svg width="36" height="36"><path d="M20 12l-6 6 6 6" fill="none" stroke="#fff" stroke-width="2.5"/></svg></div>
<div class="arrow-btn" style="left:1101px"><svg width="36" height="36"><path d="M16 12l6 6-6 6" fill="none" stroke="#fff" stroke-width="2.5"/></svg></div>

<section class="sectors">
  <div class="sector" style="left:20px">
    <div class="photo" role="img" aria-label="Wind turbines on a green field" style="background:linear-gradient(#cfe3c4,#8bb55c 60%,#4f8a2e)"></div>
    <h3>RENEWABLE ENERGY</h3>
    <p>It has survived not only five centuries, but also the leap into electronic typesetting, remaining</p>
    <span class="more">Learn More -&gt;</span>
  </div>
  <div class="sector" style="left:356px">
    <div class="photo" role="img" aria-label="Solar panels under a blue sky" style="background:linear-gradient(#4d8fd6,#9cc2ea 45%,#3a5fa8 70%,#5c9b3c)"></div>
    <h3>PROCESS AUTOMATION</h3>
    <p>It has survived not only five centuries, but also the leap into electronic typesetting, remaining</p>
    <span class="more">Learn More -&gt;</span>
  </div>
  <div class="sector" style="left:689px">
    <div class="photo" role="img" aria-label="Light bulb with a tree and solar panels at sunset" style="background:radial-gradient(circle at 50% 40%,#ffe38a,#f0a23a 45%,#b5521c 85%)"></div>
    <h3>GENERAL ENGINEERING</h3>
    <p>It has survived not only five centuries, but also the leap into electronic typesetting, remaining</p>
    <span class="more">Learn More -&gt;</span>
  </div>
</section>

<section class="welcome">
  <h2>WELCOME TO VELKOR POWER CONSULTING</h2>
  <p>We are the solar experts in the solar kingdom. The KSA (Saudi Arabia) solar market is a promising market with huge potential. The plan is to build 41,000 MW of solar in the coming 20 years, as announced by N.S.E.A. (National Solar Energy Agency). We provide our services, both by our in-house team and associated partners. All together have diversified expertise covering various aspects of solar PV. We cover all technology, market and finance related</p>
  <div class="readmore">Read More »</div>
  <div class="frame"><div class="photo" role="img" aria-label="Solar panels and wind turbines on green hills" style="left:2px;top:2px;width:450px;height:252px;background:linear-gradient(#dfe9f2,#9dc1dc 30%,#5f8f4a 55%,#3c5f8c 80%,#4c7a30)"></div></div>
</section>

<h2 class="section-title" style="top:1458px;font-size:31px">OUR PROJECTS</h2>
<div class="section-title" style="top:1496px;font-size:19px;color:var(--muted)">Neque porro quisquam est qui dolorem</div>
<svg class="abs" style="left:52px;top:1630px" width="24" height="40"><path d="M20 2L4 20l16 18" fill="none" stroke="#aaa" stroke-width="2"/></svg>
<svg class="abs" style="left:1124px;top:1630px" width="24" height="40"><path d="M4 2l16 18L4 38" fill="none" stroke="#aaa" stroke-width="2"/></svg>
<div class="project" style="left:92px"><div class="photo" role="img" aria-label="Solar array before city towers" style="background:linear-gradient(#c9d9e6,#7f93a6 45%,#3a5c8f 70%,#4a7a3a)"></div><div class="cap">NSEA SOLAR ATLAS</div></div>
<div class="project" style="left:351px"><div class="photo" role="img" aria-label="Couple in front of a house with rooftop solar panels" style="background:linear-gradient(#a8c8e8,#d8d2c4 55%,#6f8a4c)"></div><div class="cap">MRH ENERGY EFFICIENCY</div></div>
<div class="project" style="left:603px"><div class="photo" role="img" aria-label="Solar panels and a wind turbine under blue sky" style="background:linear-gradient(#3f7fc9,#8fb8e4 45%,#27477f 75%,#3c70b0)"></div><div class="cap">ELECTRICAL GROUNDING...</div></div>
<div class="project" style="left:868px"><div class="photo" role="img" aria-label="Hands on a laptop beside solar panels" style="background:linear-gradient(90deg,#e9dcc5,#c9c4bc 50%,#4e5a6c)"></div><div class="cap">CTI ENERGY EFFICIENCY...</div></div>

<section class="news">
  <h2 class="section-title" style="top:60px;font-size:26px">LATEST NEWS</h2>
  <div class="item" style="left:91px">
    <div class="photo" role="img" aria-label="Wind turbines at sunset" style="background:linear-gradient(#e9e2cf,#bfa57a 55%,#4a4030)"></div>
    <div class="body">
      <h4>Nemo Enim Ipsam Volup</h4>
      <div class="date">09-07-2017</div>
      <p>Lorem Ipsum has been the industry's standard dummy text ever since the 1500s, when an unknown printer took a galley of type and scrambled it to make a type specimen</p>
      <span class="link">Read More &gt;&gt;</span>
    </div>
  </div>
  <div class="item" style="left:630px;top:115px">
    <div class="photo" role="img" aria-label="Earth globe on green grass under blue sky" style="background:radial-gradient(circle at 50% 45%,#4a86c9,#2a5c9a 40%,#9ccbea 65%,#4c9a3a)"></div>
    <div class="body">
      <h4>Nemo Enim Ipsam Volup</h4>
      <div class="date">09-07-2017</div>
      <p>Lorem Ipsum has been the industry's standard dummy text ever since the 1500s, when an unknown printer took a galley of type and scrambled it to make a type specimen</p>
      <span class="link">Read More &gt;&gt;</span>
    </div>
  </div>
</section>

<footer class="footer">
  <div class="brand" style="top:100px;left:91px"><span class="dot"></span>VELKOR</div>
  <h5 style="left:356px">CONTACT US</h5>
  <div class="col" style="left:356px;top:87px">Address : 12 Harlow Lane, Eastfield<br>Corby, Cx4 2LM<br>Phone : 555-014-2876.<br>Email : info@velkorpower.com</div>
  <h5 style="left:656px">SIGN UP FOR NEWSLETTER</h5>
  <div class="col" style="left:656px;top:88px;width:200px;line-height:19px;font-size:11.5px">Your about us information would fit here nicely.</div>
  <div class="email">Email address</div>
  <div class="submit">Submit</div>
  <h5 style="left:948px">FOLLOW US OUT THERE</h5>
</footer>
<div class="social" style="left:948px"></div>
<div class="social" style="left:986px"></div>
<div class="social" style="left:1024px"></div>
<div class="social" style="left:1062px"></div>

<div class="bottom">Copyright © 2017. All Rights Reserved</div>

</body>
</html>
```